Business Card Design

Please see my website www.qvloreming.com.au to for further information on my services and styling of my site

Reason: Deadline is extended to permit alterations to current designs or for any new submissions. Cheers

Industry/Entity Type

Business

Contact Information for Business Card

Marcus Thorne
Empowerment Coach

'Live your passion'

marcus@qvtraining.com.au
0437158204
qvtraining.com.au

```html
<!DOCTYPE html>
<html lang="en">
<head>
<meta charset="utf-8">
<title>Quest Vitality Training – Business Card</title>
<link rel="stylesheet" href="https://fonts.googleapis.com/css2?family=Comfortaa:wght@400;700&family=Josefin+Sans:wght@300;400&family=Ubuntu+Condensed&display=swap">
<style>
  :root {
    --backdrop: #d9d9d9;
    --card-white: #ffffff;
    --card-dark: #1f1f1f;
    --lime: #a9cd1e;
    --grey-text: #9a9a9a;
    --light-text: #c8c8c8;
  }
  html, body {
    margin: 0;
    width: 1200px;
    height: 900px;
    overflow: hidden;
    background: var(--backdrop);
  }
  .canvas {
    position: relative;
    width: 1200px;
    height: 900px;
  }
  .card {
    position: absolute;
    left: 280px;
    width: 640px;
    height: 390px;
    border-radius: 22px;
    box-shadow: 0 10px 28px rgba(0,0,0,0.22);
    overflow: hidden;
  }
  .card--front {
    top: 45px;
    background: var(--card-white);
  }
  .card--back {
    top: 465px;
    background: var(--card-dark);
  }

  /* Front */
  .brand-lockup {
    position: absolute;
    left: 0;
    right: 0;
    top: 160px;
    display: flex;
    justify-content: center;
    align-items: center;
    gap: 16px;
  }
  .brand-mark {
    width: 22px;
    height: 22px;
    border-radius: 50%;
    background: var(--lime);
  }
  .brand-name {
    font-family: "Ubuntu Condensed", sans-serif;
    font-size: 40px;
    color: var(--lime);
    letter-spacing: 0.5px;
  }

  /* Back */
  .tagline {
    position: absolute;
    left: 40px;
    top: 40px;
    margin: 0;
    font-family: "Comfortaa", sans-serif;
    font-weight: 700;
    font-size: 36px;
    letter-spacing: 3px;
    color: var(--lime);
  }
  .back-brand {
    position: absolute;
    right: 30px;
    top: 110px;
    padding-bottom: 6px;
    border-bottom: 2px solid var(--card-white);
    font-family: "Ubuntu Condensed", sans-serif;
    font-size: 20px;
    color: var(--card-white);
  }
  .person {
    position: absolute;
    left: 40px;
    top: 175px;
  }
  .person-name {
    margin: 0;
    font-family: "Josefin Sans", sans-serif;
    font-weight: 400;
    font-size: 40px;
    color: var(--lime);
    letter-spacing: 1px;
  }
  .person-role {
    margin: 2px 0 0 4px;
    font-family: "Josefin Sans", sans-serif;
    font-weight: 300;
    font-size: 14px;
    letter-spacing: 3px;
    color: var(--grey-text);
  }
  .divider {
    position: absolute;
    left: 330px;
    top: 225px;
  }
  .contact {
    position: absolute;
    left: 370px;
    top: 275px;
    margin: 0;
    font-family: "Josefin Sans", sans-serif;
    font-size: 16px;
    line-height: 22px;
  }
  .contact-row dt {
    display: inline;
    color: var(--lime);
  }
  .contact-row dd {
    display: inline;
    margin: 0 0 0 6px;
    color: var(--light-text);
  }
</style>
</head>
<body>
<main class="canvas">
  <section class="card card--front" aria-label="Card front">
    <div class="brand-lockup">
      <span class="brand-mark"></span>
      <span class="brand-name">Quest Vitality Training</span>
    </div>
  </section>

  <section class="card card--back" aria-label="Card back">
    <h1 class="tagline">Live your passion</h1>
    <div class="back-brand">Quest Vitality Training</div>

    <div class="person">
      <h2 class="person-name">Marcus Thorne</h2>
      <p class="person-role">EMPOWERMENT COACH</p>
    </div>

    <svg class="divider" width="30" height="60" viewBox="0 0 30 60" aria-hidden="true">
      <defs>
        <linearGradient id="divider-glow" x1="0" y1="0" x2="0" y2="1">
          <stop offset="0" stop-color="#a9cd1e" stop-opacity="0"/>
          <stop offset="0.5" stop-color="#a9cd1e" stop-opacity="0.8"/>
          <stop offset="1" stop-color="#a9cd1e" stop-opacity="0"/>
        </linearGradient>
      </defs>
      <line x1="26" y1="2" x2="4" y2="58" stroke="url(#divider-glow)" stroke-width="1.5"/>
    </svg>

    <dl class="contact">
      <div class="contact-row"><dt>phone:</dt><dd>0437158204</dd></div>
      <div class="contact-row"><dt>email:</dt><dd>marcus@qvtraining.com.au</dd></div>
      <div class="contact-row"><dt>web:</dt><dd>qvtraining.com.au</dd></div>
    </dl>
  </section>
</main>
</body>
</html>
```